Clean and modern business cards

Looking for an updated business card design for my dental office “corvanta dental” . Looking for a modern clean / sleek design . I’m thinking black background but open to seeing other options . One side needs to have an appointment card . Card needs to have logo, dentist name , phone, email , address . I’ve attached couple of cards I thought were cool as well as my logo
Target Market(s)
Dental patients
Industry/Entity Type
Dentistry
Contact Information for Business Card
Phone email address

```html
<!DOCTYPE html>
<html lang="en">
<head>
<meta charset="utf-8">
<title>Corvanta Dental – Business Card</title>
<link rel="stylesheet" href="https://fonts.googleapis.com/css2?family=Montserrat:wght@400;500;700&display=swap">
<style>
  :root {
    --page: #e4e4e4;
    --card: #161616;
    --card-edge: #222222;
    --white: #f4f4f4;
    --muted: #6e6e6e;
    --body-text: #c9c9c9;
    --green: #7fb241;
    --gold: #d6a72b;
    --dots: #9a9a9a;
  }
  * { box-sizing: border-box; margin: 0; padding: 0; }
  html, body {
    width: 1200px;
    height: 1017px;
    overflow: hidden;
    background: var(--page);
    font-family: "Montserrat", Arial, sans-serif;
  }
  .sheet {
    width: 1200px;
    height: 1017px;
    display: flex;
    flex-direction: column;
    align-items: center;
    justify-content: center;
    gap: 50px;
  }
  .card {
    width: 700px;
    height: 400px;
    background: radial-gradient(circle at 30% 60%, var(--card-edge), var(--card) 70%);
    border-radius: 4px;
    box-shadow: 0 10px 30px rgba(0,0,0,0.18);
    position: relative;
    overflow: hidden;
  }

  /* Front */
  .card--front {
    display: flex;
    flex-direction: column;
    align-items: center;
    justify-content: center;
    gap: 34px;
  }
  .brand {
    display: flex;
    align-items: center;
    gap: 20px;
  }
  .brand__dot {
    width: 58px;
    height: 58px;
    border-radius: 50%;
    background: var(--white);
  }
  .brand__name {
    color: var(--white);
    font-weight: 700;
    font-size: 44px;
    letter-spacing: 1px;
    text-transform: uppercase;
    line-height: 1;
  }
  .dentist-name {
    color: var(--muted);
    font-weight: 500;
    font-size: 24px;
    letter-spacing: 1.5px;
    text-transform: uppercase;
  }

  /* Back */
  .card--back {
    padding: 62px 64px 48px 70px;
  }
  .appointment__title {
    color: var(--green);
    font-weight: 500;
    font-size: 22px;
    margin-bottom: 34px;
  }
  .appointment__field {
    display: flex;
    align-items: flex-end;
    color: var(--body-text);
    font-size: 17px;
    margin-bottom: 22px;
    width: 330px;
  }
  .appointment__field span { margin-right: 8px; }
  .appointment__field i {
    flex: 1;
    border-bottom: 2px dotted var(--dots);
    transform: translateY(-4px);
  }
  .policy {
    color: var(--body-text);
    font-size: 16px;
    line-height: 1.4;
    width: 330px;
    margin-top: 34px;
  }
  .contact {
    position: absolute;
    left: 70px;
    bottom: 40px;
    color: var(--gold);
    font-size: 16px;
    line-height: 1.45;
  }
  .contact .sep { color: var(--body-text); margin: 0 10px; }
</style>
</head>
<body>
<main class="sheet">
  <section class="card card--front" aria-label="Card front">
    <div class="brand">
      <span class="brand__dot"></span>
      <span class="brand__name">Corvanta Dental</span>
    </div>
    <p class="dentist-name">Dr. Elias Varnek</p>
  </section>

  <section class="card card--back" aria-label="Appointment card">
    <h2 class="appointment__title">Your Next Appointment is:</h2>
    <div class="appointment__field"><span>Date</span><i></i></div>
    <div class="appointment__field"><span>Time</span><i></i></div>
    <p class="policy">To cancel or reschedule please notify us at least 48 hours prior to your scheduled appointment</p>
    <address class="contact">
      2240 Harrow Road, Winnipeg, MB<span class="sep">|</span>(204) 555-0182<br>
      Corvantawpg.ca<span class="sep">|</span>contact@corvantawpg.ca
    </address>
  </section>
</main>
</body>
</html>
```